Company notecard redesign

We'd like a redesign done of our company notecards. We use these cards to hand-write messages to clients/potential clients. This could be thank-you cards, congratulations cards, check-in cards, etc. Current cards are 5.5" x 8.5" and fold in half (you'll see the fold mark on the scanned image). We would like the new cards to not fold, and just be 5.5" x 4.25". We do like the little dog head you'll see on the inside notecard scan as the dog is our logo. I've also attached our "professional" logo with our new tagline. Address info you see on the outside notecard scan is correct.

Target Market(s)

Salesforce and CRM clients

Industry/Entity Type

It Company

Colors
3377b5
ffffff
fff8ef

Requirements
Must have
• Our logo, some contact info
Nice to have
• Dog head from our current notecard scan

```html
<!DOCTYPE html>
<html lang="en">
<head>
<meta charset="utf-8">
<title>Branwell Notecards</title>
<link rel="stylesheet" href="https://fonts.googleapis.com/css2?family=Open+Sans:wght@400;600;700&display=swap">
<style>
  :root {
    --board: #1b1b1b;
    --paper: #ffffff;
    --navy: #0e3050;
    --slate: #5a6470;
    --sky: #7aaccc;
    --sky-light: #a9cbe0;
    --art-light: #d6eef9;
    --art-mid: #8fd0ef;
    --art-deep: #4a9ad6;
  }
  * { margin: 0; padding: 0; box-sizing: border-box; }
  html, body {
    width: 1200px; height: 960px; overflow: hidden;
    background: var(--board);
    font-family: "Open Sans", Arial, sans-serif;
  }
  .board { position: relative; width: 1200px; height: 960px; }
  .card {
    position: absolute; width: 528px; height: 408px;
    background: var(--paper); overflow: hidden;
    box-shadow: 0 2px 8px rgba(0,0,0,.5);
  }

  /* Front card */
  .card--front { left: 60px; top: 61px; }
  .front__art {
    position: absolute; left: 0; top: 0; width: 100%; height: 268px;
    background:
      radial-gradient(circle at 30% 25%, var(--art-mid) 0 22%, transparent 23%),
      radial-gradient(circle at 55% 85%, var(--art-light) 0 22%, transparent 23%),
      linear-gradient(135deg, var(--art-light) 0%, var(--art-mid) 45%, var(--art-deep) 100%);
  }
  .front__brand {
    position: absolute; left: 123px; top: 280px;
    display: flex; align-items: center; gap: 10px;
  }
  .brand-name {
    font-weight: 700; font-size: 58px; line-height: 1;
    letter-spacing: 2px; color: var(--navy);
  }
  .brand-dot {
    width: 58px; height: 58px; border-radius: 50%; background: var(--sky);
  }
  .front__tagline {
    position: absolute; left: 123px; top: 363px;
    font-size: 14.5px; letter-spacing: 1.6px; color: var(--slate);
  }

  /* Inside / writing card */
  .card--writing { left: 60px; top: 492px; }
  .writing__band {
    position: absolute; left: 0; bottom: 0; width: 100%; height: 28px;
  }
  .writing__name {
    position: absolute; left: 0; bottom: -7px; padding-right: 8px;
    background: var(--paper);
    font-weight: 700; font-size: 32px; line-height: 1;
    letter-spacing: 1px; color: var(--sky);
  }
  .writing__strip {
    position: absolute; left: 112px; bottom: 0; width: 362px; height: 22px;
    background: var(--sky); color: var(--paper);
    font-weight: 600; font-size: 14px; letter-spacing: 1.4px;
    line-height: 22px; padding-left: 10px;
  }
  .writing__dot {
    position: absolute; right: -24px; bottom: -44px;
    width: 110px; height: 110px; border-radius: 50%; background: var(--sky);
  }

  /* Back card */
  .card--back { left: 612px; top: 276px; background: var(--sky); }
  .back__seal {
    position: absolute; left: 137px; top: 64px;
    width: 254px; height: 254px; border-radius: 50%;
    background: var(--paper);
    border: 23px solid var(--sky-light);
    display: flex; align-items: center; justify-content: center;
  }
  .back__seal .brand-name { font-size: 34px; color: var(--sky); }
  .back__contact {
    position: absolute; left: 18px; bottom: 15px;
    font-weight: 600; font-size: 13.5px; letter-spacing: .6px;
    color: var(--paper); text-transform: uppercase; word-spacing: 1px;
  }
</style>
</head>
<body>
<main class="board">
  <section class="card card--front">
    <div class="front__art" role="img" aria-label="Soft blue illustration of rounded cloud shapes and geometric forms"></div>
    <div class="front__brand">
      <span class="brand-name">BRANWELL</span>
      <span class="brand-dot"></span>
    </div>
    <p class="front__tagline">A CLOUD CONSULTING COMPANY</p>
  </section>

  <section class="card card--writing">
    <div class="writing__band">
      <div class="writing__strip">A CLOUD CONSULTING COMPANY</div>
      <span class="writing__name">BRANWELL</span>
    </div>
    <span class="writing__dot"></span>
  </section>

  <section class="card card--back">
    <div class="back__seal"><span class="brand-name">BRANWELL</span></div>
    <p class="back__contact">branwelltech.com / 555.014.2730 / 1180 N Maple Ave Fairview IN 40012</p>
  </section>
</main>
</body>
</html>
```